We need a large 10' x 2 1/2' banner to hang from our 10x10 red canopy. It will be used for events to let people know who we are and to promote our business. Our business is called Silver Lantern Melody Tutoring. We offer private music lessons in students' homes and our target market is moms of kids ages 5-15. The canopy we are using is red and the colors we use for our business are red white and black. Other colors may be used, as long as the red, black and white are prominent.
I would like the background to be mostly white since it will contrast the red canopy and red table cloth.
I would like my logo to be somewhere on the banner. The problem is that I only have a low quality image of my logo. I will attach the logo, but if there is any way you can adjust the logo so it doesn't look blurred or pixelated, it would be greatly appreciated.
The part I would like to be most visible is "Music Lessons in Your Home". That will help people know right away what service we offer.
I would also like to include the instruments we teach. They are: piano, voice, guitar, woodwinds, brass, percussion. I picture these words across the bottom of the banner in horizontal orientation with round dots separating the instruments, but not necessarily. They can be placed in whatever way is most visually appealing.
Lastly, if there is room, I'd like to include the words, "We make it easy to provide an outstanding music education for your kids." If it looks too cluttered, it can be left out.
The specifications have also been attached as an image.
Moms of kids ages 5-15
Business

```html
<!DOCTYPE html>
<html lang="en">
<head>
<meta charset="utf-8">
<title>Silver Lantern Melody Tutoring – Event Banner</title>
<link rel="stylesheet" href="https://fonts.googleapis.com/css2?family=Open+Sans:ital,wght@0,400;0,600;1,700&display=swap">
<style>
  :root {
    --stage: #bdbec0;
    --paper: #f5f5f5;
    --paper-light: #ffffff;
    --brand-red: #d51f26;
    --ink: #111111;
    --white: #ffffff;
    --decor-tone: #e9e9e9;
  }
  * { box-sizing: border-box; margin: 0; padding: 0; }
  html, body {
    width: 1200px; height: 454px; overflow: hidden;
    background: var(--stage);
    font-family: "Open Sans", Arial, sans-serif;
  }
  .banner {
    position: absolute; left: 95px; top: 95px;
    width: 1000px; height: 248px; overflow: hidden;
    background: linear-gradient(90deg, var(--paper) 0%, var(--paper-light) 60%, var(--paper) 100%);
  }
  .background-art {
    position: absolute; left: 360px; top: 0; width: 640px; height: 248px;
    background: radial-gradient(ellipse at 55% 40%, var(--decor-tone) 0%, rgba(233,233,233,0) 70%);
    opacity: .7;
  }
  .photo-frame { position: absolute; left: 0; top: 0; width: 420px; height: 248px; }
  .lessons-badge {
    position: absolute; left: 395px; top: 28px;
    width: 130px; height: 130px; border-radius: 50%;
    background: var(--ink); color: var(--white);
    display: flex; align-items: center; justify-content: center; text-align: center;
    font-size: 15.5px; line-height: 1.3; text-transform: uppercase;
  }
  .brand {
    position: absolute; right: 22px; top: 24px;
    display: flex; align-items: center; gap: 10px;
  }
  .brand-mark { width: 14px; height: 14px; background: var(--brand-red); }
  .brand-name {
    color: var(--brand-red); font-weight: 600; font-size: 21px; line-height: 1.15;
    text-align: left;
  }
  .tagline {
    position: absolute; right: 23px; top: 130px;
    text-align: right; color: var(--ink);
    font-style: italic; font-weight: 700; font-size: 19px; line-height: 1.45;
  }
  .instrument-bar {
    position: absolute; left: 375px; right: 0; top: 202px; height: 31px;
    background: var(--brand-red); color: var(--white);
    display: flex; align-items: center; justify-content: flex-end; padding-right: 22px;
    font-size: 14.5px; letter-spacing: 1.4px; text-transform: uppercase; white-space: nowrap;
  }
  .instrument-bar .dot { margin: 0 9px; font-size: 12px; }
</style>
</head>
<body>
  <main class="banner">
    <div class="background-art" role="img" aria-label="Faint line-art of musical instruments and notes"></div>

    <div class="instrument-bar">
      <span>Piano</span><span class="dot">●</span><span>Voice</span><span class="dot">●</span><span>Guitar</span><span class="dot">●</span><span>Woodwinds</span><span class="dot">●</span><span>Brass</span><span class="dot">●</span><span>Percussion</span>
    </div>

    <svg class="photo-frame" viewBox="0 0 420 248" aria-hidden="false">
      <defs>
        <linearGradient id="photo-tones" x1="0" y1="0" x2="1" y2="1">
          <stop offset="0" stop-color="#d9b58a"/>
          <stop offset="0.35" stop-color="#c96a55"/>
          <stop offset="0.65" stop-color="#e8d8c8"/>
          <stop offset="1" stop-color="#7f9bb8"/>
        </linearGradient>
      </defs>
      <path d="M0 0 H262 C345 28 395 130 368 248 H0 Z" fill="var(--brand-red)"/>
      <path d="M0 0 H250 C330 28 380 130 352 248 H0 Z" fill="var(--paper-light)"/>
      <path d="M0 0 H246 C325 30 372 130 344 248 H0 Z" fill="url(#photo-tones)"
            role="img" aria-label="Photo of smiling children playing trumpets and a violin"/>
    </svg>

    <div class="lessons-badge">Music<br>lessons in<br>your home</div>

    <div class="brand">
      <span class="brand-mark"></span>
      <span class="brand-name">Silver Lantern<br>Melody Tutoring</span>
    </div>

    <p class="tagline">We make it easy to provide an outstanding<br>music education for your kids</p>
  </main>
</body>
</html>
```